Chicago Property Management Flyer

We need a brochure/flyer to market our property management services to Chicago property owners. I believe that my preference is single page, double sided, but a bi-fold or tri-fold format may also work. I have provided our logo, and some example images in case that is helpful. Refer to our website at http://www.velmorehq.net/ for more info.

Industry/Entity Type

Property Management

Font styles to use
Sans Serif

```html
<!DOCTYPE html>
<html lang="en">
<head>
<meta charset="utf-8">
<title>Velmore Property Management Flyer</title>
<link href="https://fonts.googleapis.com/css2?family=Roboto:wght@300;400;500;700&display=swap" rel="stylesheet">
<style>
  :root {
    --bg: #ececec;
    --navy: #032a47;
    --blue-text: #1b5283;
    --cyan: #1ec0ff;
    --grey-shape: #a9a9a9;
    --band-grey: #e2e2e2;
    --body-text: #2b2b2b;
    --light-text: #d2dde6;
  }
  * { box-sizing: border-box; margin: 0; padding: 0; }
  html, body { width: 1040px; height: 1200px; overflow: hidden; }
  body { background: var(--bg); font-family: 'Roboto', sans-serif; position: relative; }

  .page { position: absolute; top: 228px; width: 480px; height: 743px; background: #fff; overflow: hidden; box-shadow: 0 2px 10px rgba(0,0,0,.12); }
  .page--front { left: 25px; }
  .page--back { left: 535px; }

  /* Front */
  .skyline { position: absolute; left: 0; top: 0; width: 480px; height: 356px;
    background: linear-gradient(180deg, #f4f6f8 0%, #e6ebee 28%, #b9c3c8 48%, #8d8a84 70%, #6e625a 100%); }
  .front-title { position: absolute; top: 36px; left: 0; width: 100%; text-align: center;
    font-weight: 300; font-size: 21px; line-height: 26px; color: var(--blue-text); }
  .front-shapes { position: absolute; left: 0; top: 0; }
  .navy-band { position: absolute; left: 0; top: 498px; width: 480px; height: 245px; background: var(--navy); }
  .brand { position: absolute; left: 205px; top: 380px; width: 200px; text-align: center; color: var(--blue-text);
    font-weight: 700; font-size: 15px; line-height: 16px; letter-spacing: .3px; }
  .brand__mark { display: block; width: 30px; height: 30px; background: var(--blue-text); margin: 0 auto 12px; }
  .brand__line--small { font-size: 10px; letter-spacing: 2.5px; }
  .front-copy { position: absolute; left: 0; top: 562px; width: 100%; text-align: center;
    color: var(--light-text); font-weight: 300; font-size: 17.5px; line-height: 21px; }
  .front-copy p + p { margin-top: 22px; }
  .front-contacts { position: absolute; left: 29px; right: 29px; top: 709px; display: flex; justify-content: space-between;
    color: #fff; font-size: 13px; }

  /* Back */
  .top-strip { position: absolute; left: 0; top: 0; width: 100%; height: 11px; background: var(--band-grey); }
  .back-title { position: absolute; left: 29px; top: 35px; font-weight: 300; font-size: 21px; color: var(--blue-text); }
  .intro { position: absolute; left: 29px; top: 77px; width: 430px; font-size: 10.6px; line-height: 16.6px; color: var(--body-text); }
  .building-photo { position: absolute; left: 29px; top: 196px; width: 438px; height: 243px;
    background: linear-gradient(180deg, #8c4a3a 0%, #9a5a47 50%, #4c6a3a 82%, #7f8f6a 100%); }
  .building-photo svg { position: absolute; left: 0; top: 0; }
  .benefits { position: absolute; left: 40px; top: 469px; list-style: none; }
  .benefits li { display: flex; align-items: center; height: 36px; font-size: 14px; color: var(--blue-text); }
  .benefits svg { margin-right: 12px; }
  .footer-band { position: absolute; left: 0; bottom: 0; width: 100%; height: 44px; background: var(--band-grey);
    display: flex; align-items: center; justify-content: center; font-size: 11px; font-weight: 500; color: var(--blue-text); }
</style>
</head>
<body>
  <section class="page page--front">
    <div class="skyline" role="img" aria-label="Aerial photo of the Chicago skyline and lakefront"></div>
    <h1 class="front-title">Managing Properties Over Chicago<br>for over a decade</h1>
    <div class="navy-band"></div>
    <svg class="front-shapes" width="480" height="743" viewBox="0 0 480 743">
      <polygon points="103,336 264,336 182,468 30,468" fill="var(--cyan)"/>
      <polygon points="71,445 158,445 220,536 132,536" fill="var(--grey-shape)" fill-opacity=".92"/>
    </svg>
    <div class="brand">
      <span class="brand__mark"></span>
      <div>VELMORE PROPERTY</div>
      <div class="brand__line--small">MANAGEMENT</div>
    </div>
    <div class="front-copy">
      <p>Managing CHA / Section 8 rentals across Chicago<br>for over a decade.</p>
      <p>Leverage our experience and expertise to succeed<br>with your properties.</p>
    </div>
    <div class="front-contacts">
      <span>312-555-0147</span>
      <span>www.velmorehq.net</span>
      <span>nora@velmorehq.net</span>
    </div>
  </section>

  <section class="page page--back">
    <div class="top-strip"></div>
    <h2 class="back-title">Housing Agency Experts</h2>
    <p class="intro">We are very experienced working with housing agencies such as Chicago Housing Agency Housing Choice Voucher program (formerly known as Section 8). Programs such as this can secure you steady rental income through government funded programs, but can be challenging to navigate the administrative systems, processes, paperwork, and inspections.&nbsp; We can ensure your properties can succeed by working as efficiently as possible through these programs.</p>
    <div class="building-photo" role="img" aria-label="Photo of brick apartment buildings with an iron fence and front lawn">
      <svg width="438" height="243" viewBox="0 0 438 243">
        <polygon points="380,0 438,0 438,60 328,243 240,243" fill="#3ec4f2" fill-opacity=".55"/>
        <polygon points="330,0 380,0 240,243 270,243" fill="#7fd8f6" fill-opacity=".35"/>
      </svg>
    </div>
    <ul class="benefits">
      <li><svg width="9" height="9" viewBox="0 0 9 9"><polygon points="3,0 9,0 6,9 0,9" fill="var(--cyan)"/></svg>Save Time and Headaches</li>
      <li><svg width="9" height="9" viewBox="0 0 9 9"><polygon points="3,0 9,0 6,9 0,9" fill="var(--cyan)"/></svg>Maximize Your Investment Assets</li>
      <li><svg width="9" height="9" viewBox="0 0 9 9"><polygon points="3,0 9,0 6,9 0,9" fill="var(--cyan)"/></svg>Increase Income</li>
      <li><svg width="9" height="9" viewBox="0 0 9 9"><polygon points="3,0 9,0 6,9 0,9" fill="var(--cyan)"/></svg>Reduce Expenses, Maximize Profits</li>
      <li><svg width="9" height="9" viewBox="0 0 9 9"><polygon points="3,0 9,0 6,9 0,9" fill="var(--cyan)"/></svg>Stay Informed</li>
      <li><svg width="9" height="9" viewBox="0 0 9 9"><polygon points="3,0 9,0 6,9 0,9" fill="var(--cyan)"/></svg>Grow Your Investment Portfolio</li>
    </ul>
    <div class="footer-band">Velmore Property Management: 1180 W. Harlan St Chicago IL 60622 312-555-0147</div>
  </section>
</body>
</html>
```